Rural contractor needs professional informative business card

We need a business card design that looks professional but also includes information about the services that the business offers.
The business is an earthmoving and transport business. All of the services offered are listed on the old card attached.
The business is aimed at farmers so the design we are after is a classic look. The card needs to include all of the information that is listed on the old card design uploaded as an attachment. We recognize that this is a lot of information to fit on a business card but it also operates as a key marketing tool so is very important to the business.
Feel free to send me your questions.
Thanks
Reason: We are having trouble deciding between all these great designs - thank you for your efforts
We would love to see some designs using red with a little white and black. Also feel free to re-design our logo if you feel it needs to be to fit your designs. Thank you

```html
<!DOCTYPE html>
<html lang="en">
<head>
<meta charset="utf-8">
<title>RB Harlow Contracting – Business Card</title>
<link rel="stylesheet" href="https://fonts.googleapis.com/css2?family=Didact+Gothic&family=Cinzel:wght@400&display=swap">
<style>
  :root{
    --bg:#1c1c1c;
    --card-black:#0b0b0b;
    --gold:#b59a45;
    --gold-dark:#8a7430;
    --ink:#111111;
    --white:#f4f4f4;
    --grey:#c9c9c9;
    --sky-dusk:#c9ccd2;
    --ground-dusk:#5e4f42;
    --sky-day:#7fa3c9;
    --wheat:#b99b6b;
  }
  *{margin:0;padding:0;box-sizing:border-box}
  html,body{width:1200px;height:871px;overflow:hidden;background:var(--bg)}
  body{font-family:"Didact Gothic",sans-serif;position:relative}

  .card{position:absolute;left:260px;width:680px;height:388px;overflow:hidden;border-radius:3px;box-shadow:0 6px 20px rgba(0,0,0,.5)}
  .card--back{top:32px;background:var(--card-black)}
  .card--front{top:451px;background:var(--card-black)}

  /* back */
  .back-photo{position:absolute;left:0;top:0;width:680px;height:260px;
    background:linear-gradient(180deg,var(--sky-day) 0%,#b8cde0 38%,#cbb285 48%,var(--wheat) 70%,#8f7550 100%)}
  .back-fade{position:absolute;left:0;top:200px;width:680px;height:70px;background:linear-gradient(180deg,rgba(11,11,11,0),rgba(11,11,11,.55))}
  .service-heading{position:absolute;top:222px;font-size:21px;letter-spacing:3px;color:var(--ink)}
  .service-heading--earth{left:34px}
  .service-heading--transport{left:390px}
  .service-list{position:absolute;top:276px;list-style:none;color:var(--grey);font-size:16px;letter-spacing:2px;line-height:24px}
  .service-list--earth{left:34px}
  .service-list--transport{left:390px}

  /* front */
  .front-photo{position:absolute;right:0;top:0;width:470px;height:388px;
    background:linear-gradient(180deg,#aeb4bf 0%,var(--sky-dusk) 45%,#8d8378 62%,var(--ground-dusk) 100%);
    -webkit-mask-image:linear-gradient(90deg,transparent 0%,#000 45%);
    mask-image:linear-gradient(90deg,transparent 0%,#000 45%)}
  .brand{position:absolute;left:46px;top:30px;color:var(--white)}
  .brand-name{font-size:34px;letter-spacing:1px;line-height:1}
  .brand-rule{width:240px;height:2px;background:var(--white);margin:8px 0 6px}
  .brand-sub{font-size:15px;letter-spacing:6px}
  .person{position:absolute;left:58px;top:124px;font-family:"Cinzel",serif;font-size:18px;letter-spacing:3px;color:var(--white)}
  .person-rule{position:absolute;left:40px;top:152px;width:230px;height:1px;background:var(--grey)}
  .address{position:absolute;left:58px;top:170px;color:var(--white);font-size:14px;letter-spacing:2px;line-height:20px;font-style:normal}
  .contact{position:absolute;left:34px;top:232px;color:var(--white);font-size:14px;letter-spacing:2px;line-height:24px;list-style:none}
  .contact li{display:flex;align-items:center;gap:12px}
  .contact svg{width:14px;height:14px;flex:none}
  .band{position:absolute;left:0;bottom:0;width:680px;height:80px}
  .tagline{position:absolute;left:96px;bottom:28px;font-size:18px;letter-spacing:4px;color:var(--ink);font-weight:400}
</style>
</head>
<body>

<section class="card card--back" aria-label="Card back: services">
  <div class="back-photo" role="img" aria-label="Photo of a yellow road grader working in a harvested wheat field under blue sky"></div>
  <div class="back-fade"></div>
  <h2 class="service-heading service-heading--earth">Earthmoving</h2>
  <h2 class="service-heading service-heading--transport">Transport</h2>
  <ul class="service-list service-list--earth">
    <li>Road Building &amp; Maintenance</li>
    <li>Poly Pipe Laying</li>
    <li>Clearing Fence Lines</li>
    <li>Sand &amp; Gravel Supply</li>
  </ul>
  <ul class="service-list service-list--transport">
    <li>Grain Carting</li>
    <li>Hay &amp; Gravel Haulage</li>
  </ul>
</section>

<section class="card card--front" aria-label="Card front: contact details">
  <div class="front-photo" role="img" aria-label="Photo of a white prime mover hauling round cotton bales at dusk"></div>

  <div class="brand">
    <div class="brand-name">RB Harlow</div>
    <div class="brand-rule"></div>
    <div class="brand-sub">CONTRACTING</div>
  </div>

  <p class="person">Rhys Harlow</p>
  <div class="person-rule"></div>

  <address class="address">54 Wattle Lane<br>Coolabah Creek 2899</address>

  <ul class="contact">
    <li>
      <svg viewBox="0 0 16 16" aria-hidden="true"><path d="M2 6c0-3 12-3 12 0l-3 1-1-2H6L5 7 2 6zM4 8h8l1 5H3z" fill="none" stroke="var(--gold)" stroke-width="1.3"/></svg>
      <span>0400 123 456</span>
    </li>
    <li>
      <svg viewBox="0 0 16 16" aria-hidden="true"><rect x="1.5" y="3.5" width="13" height="9" fill="none" stroke="var(--gold)" stroke-width="1.3"/><path d="M1.5 3.5 8 9l6.5-5.5" fill="none" stroke="var(--gold)" stroke-width="1.3"/></svg>
      <span>rhys@harlowcontracting.example</span>
    </li>
  </ul>

  <svg class="band" viewBox="0 0 680 80" preserveAspectRatio="none" aria-hidden="true">
    <path d="M0 80V38C20 14 40 8 70 8H620C650 8 665 20 680 34V80Z" fill="var(--gold)"/>
  </svg>
  <p class="tagline">Earthmoving &amp; Transport Solutions</p>
</section>

</body>
</html>
```